依頼詳細
PCとスマホデザインの両方納品をいただきますが、
まずはデザインイメージが確認しやすいPCページのみの提案をお願いします。
スマホページは当選者に納品時にお願いしたいと思います。
スマホサイズは横幅750pxのサイズで作成してください。

レスポンシブウェブデザインを意識したデザインでお願いします。

デザインに関しては、添付してあるデザインレイアウト設計シートを基にお願いします。
参考サイトのURLはデザインレイアウト設計シートに記載してあります。

画像データについては、フリー素材から流用してイメージ画像に当て込んでください。

足りない場合は、一旦他のサイトの写真をサンプルとして入れてください。
また、購入が必要な写真などを利用した場合、価格とサイト名を教えてください。
ページ数
1ページ
希望イメージ
シンプル 複雑
単色 カラフル
暗い 明るい
日常 高級
遊び心 厳粛
未来的 伝統的
女性的 男性的
納品ファイル
• イラストレーター形式 (.ai)
• フォトショップ形式 (.psd)
• PNG形式 (.png)
補足説明
上記のいずれか1つ(アウトラインありとなしの2つ)と高解像度JPGを納品お願いします。

クライアント様より選定いただきました。
一番イメージに近いものでした

ご提案ありがとうございました。
また機会がありましたら是非お願いします。

```html
<!DOCTYPE html>
<html lang="ja">
<head>
<meta charset="utf-8">
<title>小森谷製作所</title>
<link href="https://fonts.googleapis.com/css2?family=Noto+Sans+JP:wght@400;500;700&family=Noto+Serif+JP:wght@400;600;700&display=swap" rel="stylesheet">
<style>
:root{
  --blue:#3d55f2;
  --blue-soft:#6d7ff7;
  --teal:#1f6f86;
  --ink:#222;
  --grey:#666;
  --line:#cfd6dc;
  --yellow:#f8cc55;
  --shop-blue:#2f7ff2;
  --footer:#f3f3f3;
  --white:#fff;
}
*{margin:0;padding:0;box-sizing:border-box}
html,body{width:1200px;height:3748px;overflow:hidden;background:var(--white)}
body{position:relative;font-family:"Noto Sans JP",sans-serif;color:var(--ink)}
.abs{position:absolute}
.serif{font-family:"Noto Serif JP",serif}

/* header */
.site-header{left:0;top:0;width:1200px;height:300px;background:var(--white)}
.brand{left:240px;top:40px;font-size:40px;font-weight:500;color:var(--blue);letter-spacing:1px}
.tagline{left:160px;top:110px;width:380px;font-size:14px;line-height:1.8;color:var(--ink)}
.gnav{left:590px;top:100px;display:flex;gap:56px}
.gnav a{writing-mode:vertical-rl;font-family:"Noto Serif JP",serif;font-size:24px;color:var(--ink);text-decoration:none;letter-spacing:4px}

/* hero */
.hero{left:0;top:300px;width:1200px;height:640px;background:linear-gradient(160deg,#6e7480 0%,#c9cdd2 35%,#8c3d3a 60%,#3b4452 100%)}
.hero-copy{right:40px;display:block;background:rgba(20,20,20,.7);color:var(--white);font-family:"Noto Serif JP",serif;font-weight:600;padding:6px 20px;white-space:nowrap}
.hero-copy.one{top:655px;font-size:40px}
.hero-copy.two{top:735px;font-size:44px}

/* section titles */
.sec-title{left:0;width:1200px;text-align:center;font-family:"Noto Serif JP",serif;font-size:36px;color:var(--teal)}
.sec-title svg{vertical-align:-6px;margin-right:10px}
.sec-sub{left:0;width:1200px;text-align:center;font-size:16px;letter-spacing:6px;color:var(--ink)}
.btn{display:flex;align-items:center;justify-content:center;gap:22px;background:var(--teal);color:var(--white);font-family:"Noto Serif JP",serif;font-size:24px;height:54px;width:250px}

/* about */
.about-photo{left:100px;top:1185px;width:560px;height:390px;background:linear-gradient(180deg,#e8eaec,#9ea4aa 60%,#5e646b)}
.about-lead{left:700px;top:1095px;width:420px;font-family:"Noto Serif JP",serif;font-size:22px;line-height:1.7}
.about-text{left:700px;top:1205px;width:340px;font-size:14px;line-height:2}

/* panels */
.panel{top:1620px;width:590px;height:380px}
.panel.products{left:0;background:linear-gradient(135deg,#2b2b2b,#7a7a7a 50%,#222)}
.panel.cases{left:610px;background:linear-gradient(135deg,#1d2330,#5a6a80 50%,#e8e2d0 60%,#2a2f3a)}
.panel-label{font-family:"Noto Serif JP",serif;font-size:30px;color:var(--white)}
.more{border:1px solid var(--white);color:var(--white);background:rgba(0,0,0,.35);font-size:18px;width:160px;height:40px;display:flex;align-items:center;justify-content:center}

/* news */
.news-box{left:240px;top:2260px;width:720px;height:220px;background:#f6f7f8;padding:18px 60px}
.news-row{display:flex;align-items:center;gap:22px;height:37px;border-bottom:1px solid var(--line);font-size:17px}
.news-row .date{font-size:13px;color:var(--grey);width:90px}
.news-row .tag{background:var(--teal);color:var(--white);font-size:13px;padding:1px 10px}

/* shops */
.shop{top:2765px;width:380px;height:215px;color:var(--white)}
.shop.official{left:200px;background:var(--yellow)}
.shop.mall{left:608px;background:var(--shop-blue)}
.shop-name{left:140px;top:55px;font-family:"Noto Serif JP",serif;font-size:30px}
.shop-btn{left:120px;top:140px;width:200px;height:40px;border:1px solid var(--white);font-size:18px;display:flex;align-items:center;justify-content:center;gap:12px}

/* footer */
.site-footer{left:0;top:3060px;width:1200px;height:688px;background:var(--footer)}
.f-brand{left:240px;top:3120px;font-size:26px;color:var(--blue);font-weight:500}
.f-address{left:220px;top:3180px;font-size:14px;line-height:1.9;color:var(--ink)}
.f-nav{left:530px;top:3135px;display:flex;gap:22px;font-size:20px}
.f-sub{left:600px;top:3200px;display:flex;gap:70px;font-size:14px;color:var(--grey)}
.copyright{left:820px;top:3285px;font-size:10px;color:var(--grey)}
</style>
</head>
<body>

<header class="abs site-header">
  <div class="abs brand">KOMORIYA</div>
  <p class="abs tagline">創業以来３００万台出荷！<br>収納棚・保管ラック・物流機器のロングセラー<br>コモリ工業の「ラックス」</p>
  <nav class="abs gnav">
    <a href="#">事業内容</a><a href="#">製品情報</a><a href="#">採用情報</a><a href="#">会社案内</a><a href="#">お問い合わせ</a>
  </nav>
</header>

<div class="abs hero" role="img" aria-label="倉庫の保管ラックに荷物が並ぶ写真"></div>
<div class="abs hero-copy one">安心安全、作業の効率化</div>
<div class="abs hero-copy two">おかげさまで300万台突破</div>

<!-- about -->
<svg class="abs" style="left:0;top:940px" width="330" height="280"><polygon points="0,0 330,0 0,280" fill="var(--blue)"/></svg>
<svg class="abs" style="left:0;top:1280px" width="1200" height="340"><polygon points="1200,0 1200,340 640,340" fill="var(--blue-soft)"/><polygon points="1200,90 1200,340 900,340" fill="var(--blue)"/></svg>
<h2 class="abs sec-title" style="top:960px"><svg width="38" height="34" viewBox="0 0 38 34"><path d="M3 18 L14 29 L35 4" stroke="var(--ink)" stroke-width="7" fill="none"/></svg>小森谷製作所について</h2>
<div class="abs sec-sub" style="top:1018px">ABOUT</div>
<div class="abs about-photo" role="img" aria-label="倉庫内の通路と保管ラックの写真"></div>
<p class="abs about-lead">「物流と倉庫の収納・保管」の<br>効率化・安全化を提案します</p>
<p class="abs about-text">私たちは保管ラックと物流機器の設計から施工まで一貫して手がけ、現場の声に合わせた最適な収納をお届けしています。</p>
<a class="abs btn" style="left:475px;top:1485px">事業内容<svg width="50" height="12"><path d="M0 10 H46 L36 2" stroke="#fff" stroke-width="2" fill="none"/></svg></a>

<!-- panels -->
<div class="abs panel products" role="img" aria-label="金属製ラック部材の写真"></div>
<div class="abs panel cases" role="img" aria-label="溶接作業の火花の写真"></div>
<div class="abs panel-label" style="left:235px;top:1780px">製品紹介</div>
<div class="abs panel-label" style="left:845px;top:1780px">導入事例</div>
<div class="abs more" style="left:215px;top:1895px">view more</div>
<div class="abs more" style="left:825px;top:1895px">view more</div>

<!-- news -->
<svg class="abs" style="left:0;top:2440px" width="1200" height="360"><polygon points="1200,0 1200,360 870,360" fill="var(--blue)"/></svg>
<h2 class="abs sec-title" style="top:2110px"><svg width="38" height="34" viewBox="0 0 38 34"><path d="M3 18 L14 29 L35 4" stroke="var(--ink)" stroke-width="7" fill="none"/></svg>お知らせ</h2>
<div class="abs sec-sub" style="top:2168px">NEWS</div>
<div class="abs news-box">
  <div class="news-row"><span class="date">2020.01.01</span><span class="tag">NEWS</span>タイトルが入ります。タイトルが入ります。</div>
  <div class="news-row"><span class="date">2020.01.01</span><span class="tag">NEWS</span>タイトルが入ります。タイトルが入ります。</div>
  <div class="news-row"><span class="date">2020.01.01</span><span class="tag">NEWS</span>タイトルが入ります。タイトルが入ります。</div>
  <div class="news-row"><span class="date">2020.01.01</span><span class="tag">NEWS</span>タイトルが入ります。タイトルが入ります。</div>
  <div class="news-row"><span class="date">2020.01.01</span><span class="tag">NEWS</span>タイトルが入ります。タイトルが入ります。</div>
</div>
<a class="abs btn" style="left:480px;top:2508px">一覧を見る<svg width="50" height="12"><path d="M0 10 H46 L36 2" stroke="#fff" stroke-width="2" fill="none"/></svg></a>

<!-- shops -->
<div class="abs shop official">
  <svg class="abs" style="left:30px;top:45px" width="90" height="80" viewBox="0 0 90 80"><path d="M4 8 H18 L28 52 H74 L84 20 H22" stroke="#fff" stroke-width="6" fill="none"/><circle cx="34" cy="68" r="7" fill="#fff"/><circle cx="68" cy="68" r="7" fill="#fff"/></svg>
  <div class="abs shop-name">公式ショップ</div>
  <div class="abs shop-btn">購入はこちら<svg width="30" height="10"><path d="M0 8 H26 L18 2" stroke="#fff" stroke-width="2" fill="none"/></svg></div>
</div>
<div class="abs shop mall">
  <svg class="abs" style="left:40px;top:40px" width="60" height="90" viewBox="0 0 60 90"><rect x="4" y="4" width="52" height="82" rx="8" stroke="#fff" stroke-width="6" fill="none"/><circle cx="30" cy="74" r="4" fill="#fff"/></svg>
  <div class="abs shop-name">モールショップ</div>
  <div class="abs shop-btn">購入はこちら<svg width="30" height="10"><path d="M0 8 H26 L18 2" stroke="#fff" stroke-width="2" fill="none"/></svg></div>
</div>

<!-- footer -->
<footer class="abs site-footer"></footer>
<div class="abs f-brand">KOMORIYA</div>
<p class="abs f-address">〒000-0000　北海県青葉市緑町1-2-3<br>TEL 0000-00-0000<br>FAX 0000-00-0001</p>
<nav class="abs f-nav"><span>事業内容</span><span>製品情報</span><span>採用情報</span><span>会社案内</span><span>お問い合わせ</span></nav>
<div class="abs f-sub"><span>個人情報保護方針</span><span>サイトマップ</span></div>
<div class="abs copyright">© copyright komoriya all rights reserved.</div>

</body>
</html>
```